Harborline Energy - needs a business card

Harborline Energy is a U.S. based diesel sourcing and distribution company that supports American oil & gas fields through providing quality product and consistent services.

Target Market(s)

Oil and Gas

Contact Information for Business Card

The background of the card must be white to ensure the logo pops.

Font styles to use
Serif
Sans Serif

Colors

Designer to choose colors to be used in the design.

Requirements
Must have
• Front of Card: Tag line: Harborline Energy, Powering America's Oil & Gas fields.
• Not sure if you guys do this part but just in case...
• Dale Menschow
• Owner/CEO
• C:555.318.4076
• E:Dmenschow@harborlineenergy.example
• W:Harborlineenergy.example
• Locations: Servicing the Powder River, DJ basin and Bakken formations.
• Back of Card: " Frac fueling is what we do. We understand how important diesel fuel is to your operation, which is why our main service line is Frac fueling. We assure our supply and stand by our service"

```html
<!DOCTYPE html>
<html lang="en">
<head>
<meta charset="utf-8">
<title>Harborline Energy – Business Card</title>
<link href="https://fonts.googleapis.com/css2?family=Arimo:wght@400;700&display=swap" rel="stylesheet">
<style>
  :root {
    --navy: #1d3266;
    --navy-card: #1f336a;
    --red: #c8262c;
    --white: #ffffff;
    --back-text: #e6e9f2;
    --stage: #e9eaee;
  }
  * { box-sizing: border-box; margin: 0; padding: 0; }
  html, body {
    width: 1200px; height: 800px; overflow: hidden;
    background: var(--stage);
    font-family: "Arimo", Arial, sans-serif;
  }
  .sheet {
    position: relative; width: 1200px; height: 800px;
    display: flex; align-items: center; justify-content: center; gap: 40px;
  }
  .card {
    position: relative; width: 540px; height: 310px;
    box-shadow: 0 6px 18px rgba(0,0,0,0.18);
    overflow: hidden;
  }

  /* Back */
  .card-back { background: var(--navy-card); color: var(--back-text); }
  .back-mark {
    position: absolute; left: 50%; top: 50%;
    width: 230px; height: 230px; border-radius: 50%;
    transform: translate(-50%, -50%);
    background: rgba(255,255,255,0.04);
  }
  .back-content {
    position: absolute; inset: 0;
    display: flex; flex-direction: column; align-items: center; justify-content: center;
    text-align: center;
  }
  .back-wordmark {
    font-weight: 700; font-size: 26px; letter-spacing: 1px;
    text-transform: uppercase; color: var(--white);
    padding-bottom: 8px; border-bottom: 1px solid var(--white);
    margin-bottom: 14px;
  }
  .back-statement { font-size: 12.5px; line-height: 1.45; }

  /* Front */
  .card-front { background: var(--white); color: var(--navy); }
  .brand {
    position: absolute; right: 36px; top: 84px;
    display: flex; flex-direction: column; align-items: center; gap: 12px;
  }
  .brand-dot {
    width: 70px; height: 70px; border-radius: 50%; background: var(--navy);
  }
  .brand-name {
    font-weight: 700; font-size: 24px; text-transform: uppercase;
    letter-spacing: 1px; color: var(--navy); text-align: center; line-height: 1.1;
  }
  .person { position: absolute; left: 34px; top: 44px; }
  .person-name { font-size: 20px; text-transform: uppercase; color: var(--navy); }
  .person-title { font-size: 13px; color: var(--red); margin-top: 2px; }
  .locations {
    position: absolute; left: 34px; top: 114px;
    font-size: 12.5px; line-height: 1.35; color: var(--navy);
  }
  .contacts {
    position: absolute; left: 34px; top: 170px;
    list-style: none; font-size: 12.5px; line-height: 1.35;
  }
  .contact { display: flex; align-items: center; gap: 6px; }
  .contact-icon { width: 13px; height: 13px; flex: none; }
  .tagline {
    position: absolute; left: 34px; top: 240px;
    font-size: 12.5px; line-height: 1.35; color: var(--navy);
  }
</style>
</head>
<body>
<main class="sheet">

  <section class="card card-back" aria-label="Back of card">
    <div class="back-mark" aria-hidden="true"></div>
    <div class="back-content">
      <div class="back-wordmark">Harborline Energy</div>
      <p class="back-statement">
        Frac fueling is what we do.<br>
        We understand how important diesel fuel is to your operation,<br>
        which is why our main service line is Frac fueling.<br>
        We assure our supply and stand by our service
      </p>
    </div>
  </section>

  <section class="card card-front" aria-label="Front of card">
    <div class="person">
      <div class="person-name">Dale Menschow</div>
      <div class="person-title">Owner/CEO</div>
    </div>

    <p class="locations">Servicing the Powder River,<br>DJ basin and Bakken formations.</p>

    <ul class="contacts">
      <li class="contact">
        <svg class="contact-icon" viewBox="0 0 16 16" aria-hidden="true">
          <circle cx="8" cy="8" r="8" fill="var(--red)"/>
          <path d="M5.2 4.2l1.4-.3.8 2-1 .7c.5 1.2 1.3 2 2.5 2.5l.7-1 2 .8-.3 1.4c-3.6.2-6.3-2.5-6.1-6.1z" fill="#fff"/>
        </svg>
        <span>555.318.4076</span>
      </li>
      <li class="contact">
        <svg class="contact-icon" viewBox="0 0 16 16" aria-hidden="true">
          <circle cx="8" cy="8" r="8" fill="var(--red)"/>
          <rect x="4" y="5" width="8" height="6" fill="none" stroke="#fff" stroke-width="1"/>
          <path d="M4 5l4 3.2L12 5" fill="none" stroke="#fff" stroke-width="1"/>
        </svg>
        <span>Dmenschow@harborlineenergy.example</span>
      </li>
      <li class="contact">
        <svg class="contact-icon" viewBox="0 0 16 16" aria-hidden="true">
          <circle cx="8" cy="8" r="8" fill="var(--red)"/>
          <circle cx="8" cy="8" r="4" fill="none" stroke="#fff" stroke-width="1"/>
          <path d="M4 8h8M8 4c-1.6 2.4-1.6 5.6 0 8M8 4c1.6 2.4 1.6 5.6 0 8" fill="none" stroke="#fff" stroke-width="0.8"/>
        </svg>
        <span>Harborlineenergy.example</span>
      </li>
    </ul>

    <p class="tagline">Harborline Energy,<br>Powering America's Oil &amp; Gas fields.</p>

    <div class="brand">
      <div class="brand-dot" aria-hidden="true"></div>
      <div class="brand-name">Harborline<br>Energy</div>
    </div>
  </section>

</main>
</body>
</html>
```